New letter head for Air Conditioning business

We need a new professional letter head design to suit our new re-branded air conditioning business. Our new logo is attached

```html
<!DOCTYPE html>
<html lang="en">
<head>
<meta charset="utf-8">
<title>Norvent Letterhead</title>
<link rel="stylesheet" href="https://fonts.googleapis.com/css2?family=Lato:wght@300;400;700&family=Pinyon+Script&display=swap">
<style>
  :root {
    --bg: #e6e6e6;
    --paper: #f3f3f3;
    --ink: #3a3a3a;
    --ink-soft: #4a4a4a;
    --ink-strong: #111111;
    --brand-green: #5fb57e;
  }
  * { margin: 0; padding: 0; box-sizing: border-box; }
  html, body {
    width: 1200px; height: 1200px; overflow: hidden;
    background: var(--bg);
    font-family: "Lato", sans-serif;
  }
  .letterhead {
    position: absolute;
    left: 211px; top: 50px;
    width: 778px; height: 1100px;
    background: var(--paper);
    box-shadow: 0 4px 18px rgba(0,0,0,0.12);
    overflow: hidden;
  }
  .brand {
    position: absolute;
    left: 509px; top: 48px;
    display: flex; align-items: center; gap: 10px;
  }
  .brand-dot {
    width: 30px; height: 30px; border-radius: 50%;
    background: var(--brand-green);
  }
  .brand-name {
    font-size: 26px; font-weight: 700; letter-spacing: 3px;
    color: var(--ink);
  }
  .sender {
    position: absolute;
    left: 509px; top: 101px;
    font-size: 12.4px; line-height: 16px; color: var(--ink);
  }
  .sender-contacts { margin-top: 7px; list-style: none; }
  .sender-contacts li { display: flex; align-items: center; gap: 6px; }
  .sender-contacts svg { width: 10px; height: 10px; flex: none; }
  .letter {
    position: absolute;
    left: 83px; top: 258px; width: 612px;
    font-size: 12.2px; font-weight: 300; line-height: 18.3px;
    color: var(--ink-soft);
  }
  .letter-date { margin-bottom: 18px; }
  .recipient { margin-bottom: 36px; }
  .recipient-name { font-weight: 700; color: var(--ink-strong); }
  .salutation { margin-bottom: 18px; }
  .letter-body p { text-align: justify; margin-bottom: 18px; }
  .closing { margin-top: 47px; }
  .signature {
    font-family: "Pinyon Script", cursive;
    font-size: 25px; font-weight: 400; color: var(--ink-strong);
    margin: 4px 0 0 6px;
  }
  .footer-band {
    position: absolute;
    left: 249px; bottom: 0;
    width: 529px; height: 18px;
    background: var(--brand-green);
    clip-path: polygon(0 0, 100% 0, 100% 100%, 10px 100%);
  }
</style>
</head>
<body>
  <main class="letterhead">
    <header>
      <div class="brand">
        <span class="brand-dot"></span>
        <span class="brand-name">NORVENT</span>
      </div>
      <address class="sender" style="font-style:normal">
        Unit 14, Level 2<br>
        Harbourline Ave<br>
        VIC, Australia 3100
        <ul class="sender-contacts">
          <li>
            <svg viewBox="0 0 10 10"><path d="M2 1l2 2-1 1.2c.6 1.2 1.6 2.2 2.8 2.8L7 6l2 2-1.3 1.3C4.5 9 1 5.5.7 2.3z" fill="var(--brand-green)"/></svg>
            (+61) 300.415.270
          </li>
          <li>
            <svg viewBox="0 0 10 10"><rect x="0.5" y="2" width="9" height="6" fill="var(--brand-green)"/><path d="M0.5 2l4.5 3.5L9.5 2" stroke="#fff" stroke-width="0.9" fill="none"/></svg>
            hello@norventair.com
          </li>
          <li>
            <svg viewBox="0 0 10 10"><circle cx="5" cy="5" r="4.3" fill="none" stroke="var(--brand-green)" stroke-width="1"/><path d="M0.8 5h8.4M5 0.8c-2.2 2.4-2.2 6 0 8.4M5 0.8c2.2 2.4 2.2 6 0 8.4" stroke="var(--brand-green)" stroke-width="0.8" fill="none"/></svg>
            www.norventair.com
          </li>
        </ul>
      </address>
    </header>

    <section class="letter">
      <p class="letter-date">01 January 2050</p>
      <p class="recipient">
        <span class="recipient-name">Company (Pvt) Ltd.</span><br>
        PO Box 3355 Mainville St<br>
        Sample City Country 3355
      </p>
      <p class="salutation">Dear Laura Pembrook,</p>
      <div class="letter-body">
        <p>Lorem ipsum dolor sit amet, consectetuer adipiscing elit, sed diam nonummy nibh euismod tincidunt ut laoreet dolore magna aliquam erat volutpat. Ut wisi enim ad minim veniam, quis nostrud exerci tation ullamcorper suscipit lobortis nisl ut aliquip ex ea commodo consequat. Duis dolore te feugait nulla facilisi. Nam liber tempor cum soluta nobis eleifend option congue nihil imperdiet doming id quod mazim placerat facer possim assum. Lorem ipsum dolor sit amet, consectetuer adipiscing elit, sed diam nonummy nibh euismod tincidunt ut laoreet dolore magna aliquam erat volutpat. Ut wisi enim ad minim veniam, quis nostrud exerci tation ullamcorper suscipit lobortis nisl ut aliquip ex ea commodo consequat.</p>
        <p>Consectetuer adipiscing elit, sed diam nonummy nibh euismod tincidunt ut laoreet dolore magna aliquam erat volutpat. Ut wisi enim ad minim veniam, quis nostrud exerci tation ullamcorper suscipit lobortis nisl ut aliquip ex ea commodo consequat. Consectetuer adipiscing elit, sed diam nonummy nibh euismod tincidunt ut laoreet dolore magna aliquam erat volutpat. Ut wisi enim ad minim veniam, quis nostrud exerci tation ullamcorper suscipit lobortis nisl ut aliquip ex ea commodo consequat.</p>
        <p>Consectetuer adipiscing elit, sed diam nonummy nibh euismod tincidunt ut laoreet dolore magna aliquam erat volutpat. Ut wisi enim ad minim veniam, quis nostrud exerci tation ullamcorper suscipit lobortis nisl ut aliquip ex ea commodo consequat. Consectetuer adipiscing elit, sed diam nonummy nibh euismod tincidunt ut laoreet dolore magna aliquam erat volutpat. Ut wisi enim ad minim veniam, quis nostrud exerci tation ullamcorper suscipit lobortis nisl ut aliquip ex ea commodo consequat.</p>
      </div>
      <p class="closing">Sincerely Yours</p>
      <p class="signature">Daniel James Whitmore</p>
    </section>

    <div class="footer-band"></div>
  </main>
</body>
</html>
```